Simple and Clean business card design

We would like the design to be simple clean and to incorporate our colors.

We are open to your design and talent, we have the dots in our logo as we think of it as data points and we connect data points for people.

We are open to see the great creative and clean design you bring to the table

Contact Information for Business Card

please include: name, position, email, phone and website

Font styles to use
Sans Serif

Requirements
Must have
• my colors incorporated, simplicity
Nice to have
• lots of white space, simplicity
Should not have
• complexicity/ complex art

```html
<!DOCTYPE html>
<html lang="en">
<head>
<meta charset="UTF-8">
<title>Nodera – Business Card</title>
<link rel="stylesheet" href="https://fonts.googleapis.com/css2?family=Montserrat:wght@400;700&family=Open+Sans:wght@400&display=swap">
<style>
  :root {
    --stage: #133a61;
    --card: #ffffff;
    --frame: #8a8a8a;
    --ink: #1b1b1b;
    --muted: #777777;
    --brand-blue: #1e88e5;
  }
  * { box-sizing: border-box; margin: 0; padding: 0; }
  html, body { width: 1200px; height: 1200px; overflow: hidden; }
  body {
    background: var(--stage);
    font-family: "Open Sans", sans-serif;
    color: var(--ink);
    position: relative;
  }
  .card {
    position: absolute;
    left: 150px;
    width: 900px;
    height: 514px;
    background: var(--card);
    box-shadow: 0 14px 40px rgba(0,0,0,0.35);
  }
  .card--back { top: 60px; }
  .card--front { top: 626px; }
  .card__frame {
    position: absolute;
    inset: 22px;
    border: 1.5px solid var(--frame);
  }

  /* Back side */
  .back__phone {
    position: absolute;
    top: 12px;
    left: 600px;
    display: flex;
    align-items: center;
    gap: 14px;
    padding: 0 16px;
    background: var(--card);
    font-size: 17px;
    letter-spacing: 1px;
    color: #444;
  }
  .back__phone svg { width: 16px; height: 16px; }
  .back__web {
    position: absolute;
    bottom: 11px;
    left: 50%;
    transform: translateX(-50%);
    padding: 0 18px;
    background: var(--card);
    font-size: 19px;
    letter-spacing: 0.5px;
    color: #333;
  }
  .wordmark {
    position: absolute;
    display: flex;
    align-items: center;
    font-family: "Montserrat", sans-serif;
    font-weight: 400;
    color: var(--ink);
    line-height: 1;
  }
  .wordmark__dot {
    border-radius: 50%;
    background: var(--brand-blue);
  }
  .back__wordmark {
    left: 50%;
    top: 50%;
    transform: translate(-50%, -50%);
    font-size: 140px;
    gap: 20px;
  }
  .back__wordmark .wordmark__dot { width: 30px; height: 30px; }

  /* Front side */
  .front__name {
    position: absolute;
    left: 70px;
    top: 74px;
    font-family: "Montserrat", sans-serif;
    font-weight: 700;
    font-size: 54px;
    letter-spacing: 1px;
    line-height: 1;
  }
  .front__name-first { color: var(--brand-blue); }
  .front__role {
    position: absolute;
    left: 72px;
    top: 138px;
    font-size: 22px;
    letter-spacing: 2px;
    color: var(--muted);
  }
  .front__contacts {
    position: absolute;
    left: 72px;
    top: 210px;
    list-style: none;
    display: flex;
    flex-direction: column;
    gap: 18px;
    font-size: 22px;
    color: #444;
  }
  .front__contacts li { display: flex; align-items: center; gap: 16px; }
  .front__contacts svg { width: 20px; height: 20px; fill: #444; }
  .front__wordmark {
    right: 64px;
    bottom: 60px;
    font-size: 62px;
    gap: 10px;
  }
  .front__wordmark .wordmark__dot { width: 14px; height: 14px; }
</style>
</head>
<body>

  <section class="card card--back" aria-label="Business card back">
    <div class="card__frame"></div>
    <div class="back__phone">
      <svg viewBox="0 0 24 24" aria-hidden="true"><path fill="#333" d="M6.6 10.8a15.1 15.1 0 0 0 6.6 6.6l2.2-2.2a1 1 0 0 1 1-.25 11.4 11.4 0 0 0 3.6.57 1 1 0 0 1 1 1V20a1 1 0 0 1-1 1A17 17 0 0 1 3 4a1 1 0 0 1 1-1h3.5a1 1 0 0 1 1 1c0 1.25.2 2.45.57 3.57a1 1 0 0 1-.25 1z"/></svg>
      <span>000 000000</span>
    </div>
    <div class="wordmark back__wordmark">
      <span class="wordmark__text">Nodera</span>
      <span class="wordmark__dot"></span>
    </div>
    <div class="back__web">www.nodera.com</div>
  </section>

  <section class="card card--front" aria-label="Business card front">
    <div class="card__frame"></div>
    <h1 class="front__name"><span class="front__name-first">NODERA</span> DEMO</h1>
    <p class="front__role">CEO</p>
    <ul class="front__contacts">
      <li>
        <svg viewBox="0 0 24 24" aria-hidden="true"><path d="M12 2a7 7 0 0 0-7 7c0 5.25 7 13 7 13s7-7.75 7-13a7 7 0 0 0-7-7zm0 9.5A2.5 2.5 0 1 1 12 6.5a2.5 2.5 0 0 1 0 5z"/></svg>
        <span>MILLBROOK, USA 00023</span>
      </li>
      <li>
        <svg viewBox="0 0 24 24" aria-hidden="true"><path d="M2 5h20v14H2zm2 2v.4l8 5.1 8-5.1V7z"/></svg>
        <span>demo@nodera.com</span>
      </li>
    </ul>
    <div class="wordmark front__wordmark">
      <span class="wordmark__text">Nodera</span>
      <span class="wordmark__dot"></span>
    </div>
  </section>

</body>
</html>
```